Business Card Design using new logo

As much as we'd like to think that treating everyone equally is the best strategy for fairness, the reality is that the differences in the lives of women and men have to be taken into account to ensure that organizations, programs, services, and yes, even public policy treat women and men in ways that achieve gender equity.

That's where ParityLoom - balance insight metrics comes in. Using the data-driven tools of gender analysis, our organization can help anyone determine if gender equity is being achieved - in businesses and organizations, in the planning and implementation of programs and services, and in the development and enforcement of public policy.
Updates

Apologies for the delay - have not had time to finalize the decision.  Should be early this week - probably Tuesday.

Industry/Entity Type

Business

Requirements
Must have
• New Logo for ParityLoom
• Logo plus words "Balance Insight Metrics"

```html
<!DOCTYPE html>
<html lang="en">
<head>
<meta charset="utf-8">
<title>ParityLoom – Business Card</title>
<link href="https://fonts.googleapis.com/css2?family=Open+Sans:wght@400;600;700&display=swap" rel="stylesheet">
<style>
  :root {
    --backdrop: #c9cacc;
    --brand-orange: #e89b45;
    --brand-orange-deep: #e08a2c;
    --card-white: #f7f7f6;
    --ink: #333538;
    --ink-soft: #55585c;
    --rule-grey: #d8d8d8;
  }
  * { margin: 0; padding: 0; box-sizing: border-box; }
  html, body {
    width: 1200px;
    height: 900px;
    overflow: hidden;
    background: var(--backdrop);
    font-family: "Open Sans", Arial, sans-serif;
  }
  .stage {
    width: 1200px;
    height: 900px;
    display: flex;
    align-items: center;
    justify-content: center;
    gap: 60px;
  }
  .card {
    position: relative;
    width: 520px;
    height: 297px;
    border-radius: 3px;
    box-shadow: 0 10px 24px rgba(0,0,0,0.18);
    overflow: hidden;
  }

  /* Front */
  .card--front {
    background: var(--brand-orange);
    color: #fff;
  }
  .front-brand {
    position: absolute;
    right: 48px;
    top: 118px;
    display: flex;
    align-items: center;
    gap: 12px;
  }
  .brand-dot {
    width: 38px;
    height: 38px;
    border-radius: 50%;
    background: #fff;
  }
  .front-brand .brand-name {
    font-size: 40px;
    font-weight: 600;
    letter-spacing: -0.5px;
    line-height: 1;
  }
  .front-url {
    position: absolute;
    right: 50px;
    top: 172px;
    font-size: 13px;
    letter-spacing: 0.6px;
  }

  /* Back */
  .card--back {
    background: var(--card-white);
    color: var(--ink);
  }
  .back-brand {
    position: absolute;
    left: 30px;
    top: 30px;
    display: flex;
    align-items: center;
    gap: 9px;
  }
  .back-brand .brand-dot {
    width: 30px;
    height: 30px;
    background: var(--brand-orange);
  }
  .back-brand .brand-name {
    font-size: 30px;
    font-weight: 600;
    letter-spacing: -0.4px;
    color: var(--ink);
    line-height: 1;
  }
  .contact {
    position: absolute;
    left: 300px;
    top: 110px;
    width: 220px;
  }
  .contact-name {
    font-size: 17px;
    font-weight: 700;
    padding-bottom: 7px;
    border-bottom: 2px solid var(--brand-orange);
  }
  .contact-list {
    list-style: none;
    margin-top: 12px;
  }
  .contact-list li {
    display: flex;
    align-items: center;
    gap: 12px;
    font-size: 11.5px;
    color: var(--ink-soft);
    height: 16px;
  }
  .contact-list svg {
    width: 10px;
    height: 10px;
    fill: var(--brand-orange-deep);
    flex-shrink: 0;
  }
  .social-dot {
    width: 9px;
    height: 9px;
    border-radius: 50%;
    background: var(--brand-orange-deep);
    flex-shrink: 0;
  }
  .base-rule {
    position: absolute;
    left: 0;
    right: 0;
    bottom: 18px;
    height: 4px;
    background: var(--brand-orange);
  }
  .base-rule--grey {
    bottom: 12px;
    height: 1px;
    background: var(--rule-grey);
  }
</style>
</head>
<body>
<main class="stage">
  <section class="card card--front" aria-label="Card front">
    <div class="front-brand">
      <span class="brand-dot"></span>
      <span class="brand-name">ParityLoom</span>
    </div>
    <p class="front-url">www.parityloom.com</p>
  </section>

  <section class="card card--back" aria-label="Card back">
    <div class="back-brand">
      <span class="brand-dot"></span>
      <span class="brand-name">ParityLoom</span>
    </div>
    <div class="contact">
      <h2 class="contact-name">Maya Lindqvist</h2>
      <ul class="contact-list">
        <li>
          <svg viewBox="0 0 10 10" aria-hidden="true"><path d="M2 0.5 L3.6 0.5 L4.2 2.8 L3.1 3.6 C3.7 5 4.9 6.3 6.4 6.9 L7.2 5.8 L9.5 6.4 L9.5 8 C9.5 9 8.7 9.5 8 9.5 C4 9.2 0.8 6 0.5 2 C0.5 1.2 1 0.5 2 0.5 Z"/></svg>
          353&nbsp; 555 0147
        </li>
        <li>
          <svg viewBox="0 0 10 10" aria-hidden="true"><path d="M2.5 0 H7.5 A0.8 0.8 0 0 1 8.3 0.8 V9.2 A0.8 0.8 0 0 1 7.5 10 H2.5 A0.8 0.8 0 0 1 1.7 9.2 V0.8 A0.8 0.8 0 0 1 2.5 0 Z M2.8 1.2 V7.6 H7.2 V1.2 Z"/></svg>
          353&nbsp; 555 0148
        </li>
        <li>
          <svg viewBox="0 0 10 10" aria-hidden="true"><path d="M0 2 H10 V8.5 H0 Z M0.6 2.4 L5 5.6 L9.4 2.4 L9.4 3.2 L5 6.4 L0.6 3.2 Z" fill-rule="evenodd"/></svg>
          hello@parityloom.com
        </li>
        <li>
          <span class="social-dot"></span>
          @Parity_Loom
        </li>
      </ul>
    </div>
    <div class="base-rule"></div>
    <div class="base-rule base-rule--grey"></div>
  </section>
</main>
</body>
</html>
```